Partial Vehicle Wrap for Vacation Rental Company

We are purchasing new 2024 Valtor Stride Hauler vans for our maintenance team and will be wrapping the vehicles. The wrap will be a partial wrap, meaning it will only cover 50% of the vehicle, the rest will be white. Our company does property management for vacation rentals in Columbia and Lake Murray SC. We have a more modern and clean aesthetic - our website is pinecovecottagesuites.com. I have uploaded our logo as an example of our colors and brand guidelines.

Target Market(s)

Lake Vacation and Family Oriented

Industry/Entity Type

Vacation rental management

Font styles to use
Sans Serif

Colors
0054AA
0677BA
7BADD7
CADEEF
E8F1F8

Requirements
Must have
• Our company name, phone number, brand colors
Nice to have
• Clean lines, modern, easy to read
Should not have
• We don't want this to be too busy, with too much going on.

```html
<!DOCTYPE html>
<html lang="en">
<head>
<meta charset="utf-8">
<title>Pinecove Cottage Suites – Van Wrap</title>
<link rel="stylesheet" href="https://fonts.googleapis.com/css2?family=Montserrat:wght@700&family=Open+Sans:wght@400;600&display=swap">
<style>
  :root {
    --paper: #ffffff;
    --wrap-white: #f7f8f9;
    --panel-edge: #d9dcdf;
    --charcoal: #4a4a4c;
    --slate: #5c5d60;
    --brand-blue: #0677ba;
    --brand-sky: #4fb0e6;
    --ink: #545456;
  }
  * { margin: 0; padding: 0; box-sizing: border-box; }
  html, body { width: 1200px; height: 2263px; overflow: hidden; background: var(--paper); }
  .canvas { position: relative; width: 1200px; height: 2263px; }
  .wrap-view { position: absolute; left: 0; width: 1200px; }
  .wrap-view svg { display: block; }
  .side-view { top: 140px; }
  .front-view { top: 900px; }
  .rear-view { top: 1470px; }
  .brand-name { font-family: "Montserrat", sans-serif; font-weight: 700; fill: var(--charcoal); }
  .brand-line { font-family: "Open Sans", sans-serif; font-weight: 400; fill: var(--ink); }
  .contact-small { font-family: "Open Sans", sans-serif; font-weight: 600; fill: var(--ink); }
  .contact-phone { font-family: "Open Sans", sans-serif; font-weight: 400; fill: var(--ink); }
</style>
</head>
<body>
<main class="canvas">

  <section class="wrap-view side-view" aria-label="Side panel wrap">
    <svg width="1200" height="480" viewBox="0 0 1200 480">
      <defs>
        <clipPath id="side-body"><rect x="45" y="30" width="1110" height="400" rx="40"/></clipPath>
      </defs>
      <g clip-path="url(#side-body)">
        <rect class="side-base" x="45" y="30" width="1110" height="400" fill="var(--wrap-white)"/>
        <path class="side-lower" d="M45 300 C220 250 420 245 620 285 C820 325 1000 280 1155 130 L1155 430 L45 430 Z" fill="var(--slate)"/>
        <path class="side-swoosh" d="M45 300 C220 250 420 245 620 285 C820 325 1000 280 1155 130" fill="none" stroke="var(--brand-blue)" stroke-width="22"/>
      </g>
      <rect x="45" y="30" width="1110" height="400" rx="40" fill="none" stroke="var(--panel-edge)" stroke-width="2"/>
      <text class="brand-name" x="1035" y="96" text-anchor="end" font-size="54" letter-spacing="7">PINECOVE</text>
      <text class="brand-line" x="537" y="145" font-size="40" letter-spacing="6">COTTAGE SUITES</text>
      <text class="brand-line" x="537" y="171" font-size="15" letter-spacing="3.6">PINECOVECOTTAGESUITES.COM</text>
      <text class="contact-small" x="577" y="200" font-size="10" letter-spacing="1.6">CONTACT@PINECOVECS.COM</text>
      <text class="contact-phone" x="572" y="236" font-size="34" letter-spacing="5">803 555 0148</text>
    </svg>
  </section>

  <section class="wrap-view front-view" aria-label="Hood wrap">
    <svg width="1200" height="180" viewBox="0 0 1200 180">
      <path class="hood-panel" d="M320 40 Q600 20 880 40 L900 150 Q600 165 300 150 Z" fill="var(--wrap-white)" stroke="var(--panel-edge)" stroke-width="2"/>
      <text class="brand-name" x="600" y="88" text-anchor="middle" font-size="34" letter-spacing="8">PINECOVE</text>
      <text class="brand-line" x="600" y="124" text-anchor="middle" font-size="26" letter-spacing="7">COTTAGE SUITES</text>
    </svg>
  </section>

  <section class="wrap-view rear-view" aria-label="Rear doors wrap">
    <svg width="1200" height="720" viewBox="0 0 1200 720">
      <defs>
        <clipPath id="rear-doors"><rect x="280" y="30" width="640" height="640" rx="50"/></clipPath>
      </defs>
      <g clip-path="url(#rear-doors)">
        <rect class="rear-base" x="280" y="30" width="640" height="640" fill="var(--slate)"/>
        <ellipse class="rear-swoosh" cx="600" cy="140" rx="325" ry="345" fill="var(--brand-sky)"/>
        <ellipse class="rear-field" cx="600" cy="120" rx="318" ry="325" fill="var(--wrap-white)"/>
      </g>
      <line x1="600" y1="30" x2="600" y2="670" stroke="#3a3a3c" stroke-width="2"/>
      <rect x="280" y="30" width="640" height="640" rx="50" fill="none" stroke="var(--panel-edge)" stroke-width="2"/>
      <text class="brand-name" x="600" y="210" text-anchor="middle" font-size="46" letter-spacing="8">PINECOVE</text>
      <text class="brand-line" x="600" y="262" text-anchor="middle" font-size="36" letter-spacing="6">COTTAGE SUITES</text>
      <text class="brand-line" x="600" y="300" text-anchor="middle" font-size="19" letter-spacing="4">PINECOVECOTTAGESUITES.COM</text>
      <text class="contact-small" x="600" y="378" text-anchor="middle" font-size="13" letter-spacing="2.5">CONTACT@PINECOVECS.COM</text>
      <text class="contact-phone" x="600" y="420" text-anchor="middle" font-size="30" letter-spacing="5">803 555 0148</text>
    </svg>
  </section>

</main>
</body>
</html>
```